Flyer for our prophetic church event

I need a flyer designed for the launching of our "Nine Radiant Lord's Day Gatherings" event. This event should high light the next 7 Sundays starting on February the 11th, 2018

Event Name:
Nine Radiant Lord's Days

Event Slogan or topic:
Go and tell John ... the blind see, the lame walk, the lepers are cleansed, the deaf hear, the dead are raised,
the poor have the gospel preached to them.

Speaker:
Prophet Tomas Okello

February 11th
February 18th
February 25th
March 4th
March 11th
March 18th
March 25th

Location:
Halvor Community Center
382 Wendle Street
Portland, ME 04102
United States

Time:
10:00AM - 12:00PM

We welcome you all in the name of Jesus Christ

Contact Info:
Tel:+1(207) 555 3184 - Email:contact@brightmeadowfold.org - Website: http://velkor.org

Target Market(s)

Young adults

Industry/Entity Type

Church

Font styles to use
Other font styles liked:
• Surprise me, I trust the designers skills

Colors

Designer to choose colors to be used in the design.

Requirements
Must have
• The Velkor logo
• Tomas Okello's picture
• The
Should not have
• The background of the Tomas Okello's picture

```html
<!DOCTYPE html>
<html lang="en">
<head>
<meta charset="utf-8">
<title>Nine Radiant Lord's Days – Flyer</title>
<link href="https://fonts.googleapis.com/css2?family=Roboto:ital,wght@0,300;0,400;0,700;0,900;1,700;1,900&display=swap" rel="stylesheet">
<style>
  :root {
    --navy: #0b3a66;
    --navy-deep: #082b4d;
    --sky: #3f86c8;
    --sky-light: #cfe6f7;
    --orange: #f39a1f;
    --yellow: #f3ea4a;
    --white: #ffffff;
    --ink: #10243a;
    --page: #ecedef;
  }
  * { box-sizing: border-box; margin: 0; padding: 0; }
  html, body { width: 680px; height: 1200px; overflow: hidden; background: var(--page); }
  body { font-family: "Roboto", Arial, sans-serif; position: relative; }

  .flyer {
    position: absolute; left: 0; top: 160px;
    width: 680px; height: 880px;
    background: var(--navy);
    overflow: hidden;
    color: var(--white);
  }
  .sky {
    position: absolute; left: 0; top: 0; width: 680px; height: 520px;
    background:
      radial-gradient(ellipse 220px 140px at 345px 110px, rgba(255,255,255,0.95), rgba(255,255,255,0) 70%),
      linear-gradient(180deg, var(--sky-light) 0%, var(--sky) 32%, #1f5f9c 55%, var(--navy) 100%);
  }
  .speaker-photo {
    position: absolute; left: 320px; top: 350px; width: 360px; height: 426px;
    background: linear-gradient(160deg, rgba(70,90,110,0.55) 0%, #16202c 55%, #0d1620 100%);
    border-radius: 170px 0 0 0;
  }

  .title { position: absolute; left: 0; top: 170px; width: 680px; }
  .title-main {
    position: absolute; left: 70px; top: 0;
    font-weight: 900; font-size: 58px; letter-spacing: 0.5px;
    color: var(--navy-deep);
    text-shadow: 3px 3px 0 var(--orange);
  }
  .title-sub {
    position: absolute; right: 140px; top: 70px;
    font-weight: 300; font-size: 62px; color: var(--ink); letter-spacing: 1px;
  }

  .scripture { position: absolute; left: 59px; top: 326px; line-height: 29px; }
  .scripture-lead { font-weight: 300; font-size: 32px; line-height: 38px; }
  .scripture-line { font-weight: 300; font-size: 23px; }
  .scripture-emph { font-weight: 700; font-style: italic; font-size: 23px; }

  .details { position: absolute; top: 568px; font-size: 15.5px; font-weight: 300; line-height: 18.5px; }
  .details h3 { font-size: 18px; font-weight: 700; color: var(--yellow); line-height: 22px; }
  .details sup { font-size: 9px; line-height: 0; vertical-align: 6px; }
  .dates { left: 59px; }
  .venue { left: 202px; }
  .venue .time-label { margin-top: 14px; }
  .venue .time { font-weight: 700; color: var(--yellow); font-size: 15.5px; }

  .speaker-label { position: absolute; right: 33px; top: 702px; text-align: right; }
  .speaker-role { font-weight: 300; font-size: 22px; }
  .speaker-name { font-weight: 900; font-style: italic; font-size: 23px; text-shadow: 1px 1px 3px rgba(0,0,0,0.7); }

  .footer-band {
    position: absolute; left: 0; top: 776px; width: 680px; height: 104px;
    background: var(--orange); color: var(--ink);
  }
  .brand-box {
    position: absolute; left: 57px; top: 744px; width: 144px; height: 136px;
    background: var(--navy);
    box-shadow: 0 6px 12px rgba(0,0,0,0.35);
    display: flex; align-items: center; justify-content: center; gap: 8px;
  }
  .brand-dot { width: 12px; height: 12px; border-radius: 50%; background: var(--orange); }
  .brand-name { font-weight: 400; font-size: 26px; color: var(--white); letter-spacing: 1px; }

  .welcome { position: absolute; left: 232px; top: 17px; font-size: 15px; font-weight: 700; line-height: 19px; }
  .welcome .lord { font-style: italic; font-size: 18px; line-height: 24px; }

  .contacts { position: absolute; left: 404px; top: 13px; list-style: none; font-size: 15px; font-weight: 400; }
  .contacts li { display: flex; align-items: center; gap: 8px; height: 23px; white-space: nowrap; }
  .contacts svg { width: 15px; height: 15px; flex: none; }
</style>
</head>
<body>
<main class="flyer">
  <div class="sky" role="img" aria-label="Bright sky with clouds and light rays and a white dove with spread wings"></div>
  <div class="speaker-photo" role="img" aria-label="Portrait of Prophet Tomas Okello in a dark suit and light blue shirt"></div>

  <h1 class="title">
    <span class="title-main">NINE RADIANT</span>
    <span class="title-sub">LORD'S DAYS</span>
  </h1>

  <section class="scripture">
    <p class="scripture-lead">Go and tell John ...</p>
    <p class="scripture-line">the blind see, the lame walk,</p>
    <p class="scripture-line">the lepers are cleansed,</p>
    <p class="scripture-line">the deaf hear,</p>
    <p class="scripture-line">the dead are raised,</p>
    <p class="scripture-emph">the poor have the gospel</p>
    <p class="scripture-emph">preached to them.</p>
  </section>

  <section class="details dates">
    <h3>Event Date:</h3>
    <p>February 11<sup>th</sup></p>
    <p>February 18<sup>th</sup></p>
    <p>February 25<sup>th</sup></p>
    <p>March 4<sup>th</sup></p>
    <p>March 11<sup>th</sup></p>
    <p>March 18<sup>th</sup></p>
    <p>March 25<sup>th</sup></p>
  </section>

  <section class="details venue">
    <h3>Location:</h3>
    <p>Halvor Community Center</p>
    <p>382 Wendle Street</p>
    <p>Portland, ME 04102</p>
    <p>United States</p>
    <h3 class="time-label">Time:</h3>
    <p class="time">10:00AM - 12:00PM</p>
  </section>

  <div class="speaker-label">
    <p class="speaker-role">Speaker:</p>
    <p class="speaker-name">Prophet Tomas Okello</p>
  </div>

  <footer class="footer-band">
    <p class="welcome">We welcome you all<br>in the name of<br><span class="lord">Jesus Christ</span></p>
    <ul class="contacts">
      <li>
        <svg viewBox="0 0 24 24"><path fill="#10243a" d="M6.6 10.8a15 15 0 0 0 6.6 6.6l2.2-2.2a1 1 0 0 1 1-.25 11.4 11.4 0 0 0 3.6.57 1 1 0 0 1 1 1V20a1 1 0 0 1-1 1A17 17 0 0 1 3 4a1 1 0 0 1 1-1h3.5a1 1 0 0 1 1 1c0 1.25.2 2.45.57 3.57a1 1 0 0 1-.25 1z"/></svg>
        <span>+1(207) 555 3184</span>
      </li>
      <li>
        <svg viewBox="0 0 24 24"><circle cx="12" cy="12" r="4" fill="none" stroke="#10243a" stroke-width="2.5"/><path d="M16 8v5a3 3 0 0 0 6 0v-1a10 10 0 1 0-4 8" fill="none" stroke="#10243a" stroke-width="2.5"/></svg>
        <span>contact@brightmeadowfold.org</span>
      </li>
      <li>
        <svg viewBox="0 0 24 24" fill="none" stroke="#10243a" stroke-width="2"><circle cx="12" cy="12" r="9"/><ellipse cx="12" cy="12" rx="4" ry="9"/><path d="M3 12h18M5 7h14M5 17h14"/></svg>
        <span>www.velkor.org</span>
      </li>
    </ul>
  </footer>

  <div class="brand-box">
    <span class="brand-dot"></span>
    <span class="brand-name">VELKOR</span>
  </div>
</main>
</body>
</html>
```